Präsentationsvorlagen für Unternehmensberatung
Zielgruppe
Unternehmensberatung für die Digitalisierung und Prozessoptimierung
KMUs und Steuerberater
Aufgabenstellung
Ansprechende Power Point Vorlage für Kunden, Steuerberater und für Webinare

```html
<!DOCTYPE html>
<html lang="de">
<head>
<meta charset="utf-8">
<title>Digitalisierung und Prozessoptimierung in der Buchhaltung – Präsentationsvorlage</title>
<link href="https://fonts.googleapis.com/css2?family=Source+Sans+3:wght@400;600;700&display=swap" rel="stylesheet">
<style>
:root{
  --navy:#123d5a;
  --navy-dark:#0d2f47;
  --taupe:#a39a8f;
  --bg:#efefef;
  --white:#ffffff;
  --ink:#2c3b47;
  --muted:#b9bec3;
  --photo-a:#8d9aa6;
  --photo-b:#3f5566;
}
*{box-sizing:border-box;margin:0;padding:0}
html,body{width:1200px;height:2640px;overflow:hidden;background:var(--bg)}
body{position:relative;font-family:"Source Sans 3",sans-serif;color:var(--ink)}

/* cover */
.cover-head{position:absolute;left:57px;top:150px;width:1084px;height:174px;background:var(--white)}
.cover-brand{position:absolute;left:0;right:0;top:45px;text-align:center;font-weight:600;font-size:84px;letter-spacing:2px;color:var(--navy);line-height:1}
.cover-band{position:absolute;left:57px;top:324px;width:1084px;height:434px;background:var(--navy);color:var(--white);text-align:center}
.cover-title{margin-top:52px;font-weight:400;font-size:46px;line-height:58px;letter-spacing:.5px}
.cover-title b{color:var(--taupe);font-weight:700}
.cover-sub{margin-top:22px;font-size:24px}
.cover-author{margin-top:80px;font-weight:600;font-size:24px}

/* grid */
.deck{position:absolute;left:57px;top:813px;width:1090px;display:grid;grid-template-columns:repeat(3,354px);grid-auto-rows:200px;column-gap:14px;row-gap:12px}
.slide{position:relative;background:var(--white);overflow:hidden;font-size:6.5px;line-height:1.35}
.brand{position:absolute;top:10px;right:33px;font-weight:600;font-size:11px;color:var(--navy);line-height:1}
.brand.on-dark{color:var(--white)}
.pg{position:absolute;top:10px;right:12px;width:16px;height:12px;border-radius:3px;background:var(--navy);color:var(--white);font-size:6px;font-weight:600;text-align:center;line-height:12px}
.foot,.url{position:absolute;bottom:5px;font-size:4px;color:var(--muted)}
.foot{left:12px}.url{right:12px}
.on-navy .foot,.on-navy .url{color:#7f9bb0}

.h{position:absolute;font-weight:600;font-size:10px;line-height:1.2;color:var(--navy);text-transform:uppercase}
.h .tp{color:var(--taupe)}
.h.white{color:var(--white)}
.rule-l{position:absolute;left:0;width:24px;height:1px;background:var(--taupe)}
.sub{position:absolute;font-weight:700;font-size:7px;color:var(--navy);line-height:1.3}
.list{position:absolute;list-style:none}
.list li{position:relative;padding-left:8px;margin-bottom:3px}
.list li::before{content:"";position:absolute;left:1px;top:3px;width:3px;height:3px;border-radius:50%;background:var(--navy)}
.list li.pill{position:absolute;padding:5px 8px 5px 14px;margin:0}
.list li.pill::before{left:6px;top:8px}
.list.white li{color:var(--white)}
.list.white li::before{background:var(--white)}
.num{position:absolute;list-style:none}
.num li{display:flex;gap:8px;margin-bottom:5px;align-items:flex-start}
.num i{font-style:normal;flex:none;width:22px;height:7px;border-radius:2px;background:var(--navy);color:var(--white);font-size:4.5px;font-weight:700;text-align:center;line-height:7px;margin-top:1px}

.photo{position:absolute;background:linear-gradient(135deg,var(--photo-a),var(--photo-b))}
.photo.warm{background:linear-gradient(135deg,#c9bfb4,#6e7a84)}
.photo.tech{background:linear-gradient(135deg,#9fb2c2,#22455f)}
.round{border-radius:12px}
.circle{border-radius:50%}

.tab{position:absolute;background:var(--navy);color:var(--white);font-weight:600;text-transform:uppercase}
.card{position:absolute;background:var(--white);border-radius:6px;padding:6px 8px;font-size:5.5px;color:var(--ink);box-shadow:0 1px 3px rgba(0,0,0,.15)}
.pill{position:absolute;background:var(--white);border-radius:6px;font-size:5.5px;box-shadow:0 1px 3px rgba(0,0,0,.18)}
.navy-fill{position:absolute;background:var(--navy)}
.sq{position:absolute;width:10px;height:10px;background:var(--taupe)}
svg text{font-family:"Source Sans 3",sans-serif}
</style>
</head>
<body>

<header class="cover-head">
  <div class="cover-brand">veltaro</div>
</header>
<section class="cover-band">
  <h1 class="cover-title">DIGITALISIERUNG UND<br>PROZESSOPTIMIERUNG IN DER<br><b>BUCHHALTUNG</b></h1>
  <p class="cover-sub">Effizienzsteigerung und Automatisierung in der Finanzverwaltung</p>
  <p class="cover-author">Lukas Brenner 25 September 2024</p>
</section>

<main class="deck">

  <!-- 02 -->
  <section class="slide">
    <div class="brand">veltaro</div><div class="pg">02</div>
    <div class="rule-l" style="top:29px"></div>
    <div class="h" style="left:29px;top:24px">Einführung: <span class="tp">Warum Digitalisierung<br>in der Buchhaltung?</span></div>
    <div class="photo warm round" style="left:30px;top:64px;width:124px;height:112px" role="img" aria-label="Foto: zwei Kollegen arbeiten gemeinsam am Laptop"></div>
    <div class="sub" style="left:175px;top:76px">Bedeutung der Digitalisierung für<br>die Buchhaltung</div>
    <ul class="num" style="left:175px;top:112px;width:150px">
      <li><i>01</i><span>Wandel der Finanzabteilungen durch technologische Entwicklungen</span></li>
      <li><i>02</i><span>Herausforderung traditioneller Prozesse (Papierarbeit, manuelle Eingaben)</span></li>
    </ul>
    <div class="foot">Digitalisierung und Prozessoptimierung in der Buchhaltung</div><div class="url">www.veltaro.de</div>
  </section>

  <!-- 03 -->
  <section class="slide">
    <div class="brand">veltaro</div><div class="pg">03</div>
    <div class="rule-l" style="top:29px"></div>
    <div class="h" style="left:29px;top:24px">Einführung: <span class="tp">Warum Digitalisierung<br>in der Buchhaltung?</span></div>
    <div class="sub" style="left:30px;top:72px;font-weight:600">Kernfragen des Webinars</div>
    <ul class="num" style="left:30px;top:96px;width:160px">
      <li><i>01</i><span>Warum ist die Digitalisierung der Buchhaltung wichtig?</span></li>
      <li><i>02</i><span>Welche Prozesse lassen sich optimieren?</span></li>
      <li><i>03</i><span>Welche Technologien stehen zur Verfügung?</span></li>
      <li><i>04</i><span>Was sind die praktischen Auswirkungen?</span></li>
    </ul>
    <div class="photo warm round" style="left:206px;top:64px;width:124px;height:112px" role="img" aria-label="Foto: zwei Kollegen arbeiten gemeinsam am Laptop"></div>
    <div class="foot">Digitalisierung und Prozessoptimierung in der Buchhaltung</div><div class="url">www.veltaro.de</div>
  </section>

  <!-- 04 -->
  <section class="slide">
    <div class="brand">veltaro</div><div class="pg">04</div>
    <div class="photo tech round" style="left:18px;top:58px;width:168px;height:112px" role="img" aria-label="Bild: Hand berührt digitale Symbole, Thema digitale Transformation"></div>
    <div class="tab" style="left:0;top:20px;width:165px;height:52px;border-radius:0 0 12px 0;padding:8px 0 0 25px;font-size:9.5px;line-height:1.2">Status Quo und<br>Herausforderungen<br>der Buchhaltung</div>
    <div class="sub" style="left:213px;top:62px">Traditionelle Herausforderungen<br>in der Buchhaltung</div>
    <ul class="list" style="left:213px;top:90px;width:120px">
      <li>Zeitaufwändige manuelle Prozesse</li>
      <li>Fehleranfälligkeit durch händische Eingaben</li>
      <li>Schwierigkeiten bei der Datenverfolgung und -speicherung</li>
      <li>Schnittstellenprobleme zwischen verschiedenen Softwarelösungen</li>
    </ul>
    <div class="foot">Digitalisierung und Prozessoptimierung in der Buchhaltung</div><div class="url">www.veltaro.de</div>
  </section>

  <!-- 05 -->
  <section class="slide">
    <div class="brand">veltaro</div><div class="pg">05</div>
    <div class="photo tech round" style="left:18px;top:60px;width:168px;height:112px" role="img" aria-label="Bild: Hand berührt digitale Symbole, Thema digitale Transformation"></div>
    <div class="tab" style="left:0;top:20px;width:165px;height:52px;border-radius:0 0 12px 0;padding:8px 0 0 25px;font-size:9.5px;line-height:1.2">Status Quo und<br>Herausforderungen<br>der Buchhaltung</div>
    <div class="sub" style="left:213px;top:62px">Anforderungen an eine moderne<br>Buchhaltung</div>
    <ul class="list" style="left:213px;top:90px;width:120px">
      <li>Transparenz, Genauigkeit, Effizienz</li>
      <li>Compliance und rechtliche Anforderungen</li>
      <li>Geschwindigkeit in der Entscheidungsfindung durch Echtzeit-Daten</li>
    </ul>
    <div class="foot">Digitalisierung und Prozessoptimierung in der Buchhaltung</div><div class="url">www.veltaro.de</div>
  </section>

  <!-- 06 -->
  <section class="slide on-navy">
    <div class="navy-fill" style="left:0;top:0;width:186px;height:200px"></div>
    <div class="brand">veltaro</div><div class="pg">06</div>
    <div class="h white" style="left:29px;top:56px">Technologien zur<br>Digitalisierung<br><span class="tp">in der Buchhaltung</span></div>
    <div class="sub" style="left:210px;top:44px">Wichtige digitale Technologien<br>in der Buchhaltung</div>
    <ul class="list" style="left:210px;top:72px;width:125px">
      <li>Cloud-basierte Buchhaltungssysteme (z. B. LedgerPro, FinSuite)</li>
      <li>Künstliche Intelligenz für Datenverarbeitung und Analyse</li>
      <li>Automatisierungstools für wiederkehrende Aufgaben (z. B. Robotic Process Automation, RPA)</li>
      <li>Blockchain-Technologie für sichere Transaktionen und Audits</li>
    </ul>
    <div class="foot">Digitalisierung und Prozessoptimierung in der Buchhaltung</div><div class="url">www.veltaro.de</div>
  </section>

  <!-- 07 -->
  <section class="slide on-navy">
    <div class="navy-fill" style="left:0;top:0;width:186px;height:200px"></div>
    <div class="brand">veltaro</div><div class="pg">07</div>
    <div class="h white" style="left:29px;top:56px">Technologien zur<br>Digitalisierung<br><span class="tp">in der Buchhaltung</span></div>
    <div class="sub" style="left:210px;top:86px">Cloud-Software und<br>ihre Vorteile</div>
    <ul class="list" style="left:210px;top:112px;width:125px">
      <li>Zugriff von überall, Echtzeit-Updates, Automatische Backups</li>
      <li>Reduzierung der IT-Kosten und Verbesserung der Datensicherheit</li>
    </ul>
    <div class="foot">Digitalisierung und Prozessoptimierung in der Buchhaltung</div><div class="url">www.veltaro.de</div>
  </section>

  <!-- 08 -->
  <section class="slide">
    <div class="photo" style="left:0;top:0;width:354px;height:112px;background:linear-gradient(90deg,var(--navy) 0%,var(--navy) 40%,#8c9aa6 75%,#c7c2bb 100%)" role="img" aria-label="Foto: Team bespricht sich vor einem Laptop"></div>
    <div class="rule-l" style="top:74px;background:var(--white)"></div>
    <div class="h white" style="left:29px;top:69px">Prozessoptimierung<br><span class="tp">in der Buchhaltung</span></div>
    <div class="sub" style="left:27px;top:130px">Was bedeutet Prozess-<br>optimierung in der<br>Buchhaltung?</div>
    <ul class="list" style="left:118px;top:130px;width:222px">
      <li>Definition: Vereinfachung und Automatisierung von Aufgaben</li>
      <li>Ziele: Minimierung von Fehlern, Reduzierung von Kosten und Zeitaufwand</li>
      <li>Beispielprozesse: Rechnungsprüfung, Gehaltsabrechnungen, Steuererklärungen</li>
    </ul>
    <div class="foot">Digitalisierung und Prozessoptimierung in der Buchhaltung</div><div class="url">www.veltaro.de</div>
  </section>

  <!-- 09 -->
  <section class="slide">
    <div class="photo" style="left:0;top:0;width:354px;height:112px;background:linear-gradient(90deg,var(--navy) 0%,var(--navy) 40%,#8c9aa6 75%,#c7c2bb 100%)" role="img" aria-label="Foto: Team bespricht sich vor einem Laptop"></div>
    <div class="rule-l" style="top:74px;background:var(--white)"></div>
    <div class="h white" style="left:29px;top:69px">Prozessoptimierung<br><span class="tp">in der Buchhaltung</span></div>
    <div class="sub" style="left:27px;top:130px">Hauptprozesse, die<br>durch Digitalisierung<br>optimiert werden<br>können</div>
    <ul class="list" style="left:118px;top:130px;width:222px">
      <li>Kreditorenbuchhaltung: Automatisierung der Rechnungseingabe</li>
      <li>Debitorenbuchhaltung: Automatisiertes Mahnwesen und Zahlungsverfolgung</li>
      <li>Zahlungsabgleiche: Automatische Erkennung von Diskrepanzen</li>
    </ul>
    <div class="foot">Digitalisierung und Prozessoptimierung in der Buchhaltung</div><div class="url">www.veltaro.de</div>
  </section>

  <!-- 10 stats -->
  <section class="slide on-navy">
    <div class="navy-fill" style="left:0;top:0;width:350px;height:200px"></div>
    <div style="position:absolute;right:0;top:0;width:90px;height:40px;background:var(--white);border-radius:0 0 0 12px"></div>
    <div class="brand">veltaro</div><div class="pg">11</div>
    <div class="rule-l" style="top:29px;background:var(--white)"></div>
    <div class="h white" style="left:40px;top:24px">Statistische <span class="tp">Untermauerung</span></div>
    <div class="sub" style="left:40px;top:53px;color:var(--white);font-weight:600">Statistiken zur Digitalisierung in der Buchhaltung</div>
    <div class="card" style="left:30px;top:80px;width:96px;height:92px"><b>Fakt:</b> Laut einer Studie von Kessler Research geben 63 % der Finanzabteilungen an, dass sie ihre Produktivität durch Automatisierung um bis zu 30 % steigern konnten</div>
    <div class="card" style="left:137px;top:80px;width:96px;height:92px;color:var(--taupe)"><b style="color:var(--navy)">Fakt:</b> Laut einer Umfrage von Hartmann Consulting konnten Unternehmen durch die Digitalisierung der Buchhaltung ihre Fehlerquote um 90 % reduzieren</div>
    <div class="card" style="left:244px;top:80px;width:96px;height:92px;color:var(--taupe)"><b style="color:var(--navy)">Fakt:</b> Cloud-basierte Buchhaltungslösungen führen zu einer Kostenreduktion von bis zu 20 % im Vergleich zu traditionellen Systemen</div>
    <div class="foot">Digitalisierung und Prozessoptimierung in der Buchhaltung</div><div class="url">www.veltaro.de</div>
  </section>

  <!-- 11 case 1 -->
  <section class="slide on-navy">
    <div class="navy-fill" style="left:0;top:112px;width:354px;height:88px"></div>
    <div class="brand">veltaro</div><div class="pg">11</div>
    <div class="h" style="left:29px;top:40px">Fiktives Praxisbeispiel 1:<br><span class="tp">Automatisierung der<br>Rechnungsprüfung</span></div>
    <div class="sub" style="left:193px;top:60px">Beispiel – Automatisierung der<br>Kreditorenbuchhaltung</div>
    <div class="card" style="left:30px;top:98px;width:130px;height:24px">Firma A, ein mittelständisches Produktionsunternehmen</div>
    <div class="card" style="left:30px;top:131px;width:130px;height:32px">Ausgangslage: Manuelle Rechnungsprüfung, hohe Fehlerquoten und Zeitaufwand</div>
    <div class="card" style="left:193px;top:98px;width:135px;height:30px">Digitalisierungslösung: Einführung einer OCR-Software zur automatischen Rechnungserkennung und -verarbeitung</div>
    <div class="card" style="left:193px;top:135px;width:135px;height:24px">Ergebnis: 70 % Reduktion des Arbeitsaufwands, Fehlerquote nahezu eliminiert</div>
    <div class="foot">Digitalisierung und Prozessoptimierung in der Buchhaltung</div><div class="url">www.veltaro.de</div>
  </section>

  <!-- 12 chart -->
  <section class="slide">
    <div class="brand">veltaro</div><div class="pg">11</div>
    <svg style="position:absolute;left:0;top:0" width="354" height="200" viewBox="0 0 354 200">
      <g font-size="5" fill="#2c3b47">
        <text x="90" y="44" text-anchor="middle" font-size="6">Arbeitsaufwand (in %)</text>
        <text x="246" y="44" text-anchor="middle" font-size="6">Fehlerquote (in %)</text>
        <text x="51" y="110" transform="rotate(-90 51 110)" text-anchor="middle">Prozent</text>
        <text x="183" y="110" transform="rotate(-90 183 110)" text-anchor="middle">Prozent</text>
      </g>
      <g stroke="#cfd3d7" stroke-width=".5">
        <line x1="64" y1="52" x2="64" y2="160"/><line x1="64" y1="160" x2="178" y2="160"/>
        <line x1="196" y1="52" x2="196" y2="160"/><line x1="196" y1="160" x2="310" y2="160"/>
      </g>
      <g font-size="4" fill="#2c3b47" text-anchor="end">
        <text x="62" y="55">100</text><text x="62" y="77">80</text><text x="62" y="98">60</text><text x="62" y="120">40</text><text x="62" y="141">20</text>
        <text x="194" y="55">100</text><text x="194" y="77">80</text><text x="194" y="98">60</text><text x="194" y="120">40</text><text x="194" y="141">20</text>
      </g>
      <rect x="70" y="53" width="45" height="107" fill="#123d5a"/>
      <rect x="127" y="128" width="45" height="32" fill="#a39a8f"/>
      <rect x="202" y="53" width="45" height="107" fill="#123d5a"/>
      <rect x="259" y="158" width="45" height="2" fill="#a39a8f"/>
      <g font-size="4" fill="#2c3b47" text-anchor="middle">
        <text x="92" y="166">Vorher</text><text x="149" y="166">Nachher</text>
        <text x="224" y="166">Vorher</text><text x="281" y="166">Nachher</text>
      </g>
    </svg>
    <div class="foot">Digitalisierung und Prozessoptimierung in der Buchhaltung</div><div class="url">www.veltaro.de</div>
  </section>

  <!-- 13 case 2 -->
  <section class="slide on-navy">
    <div class="navy-fill" style="left:0;top:112px;width:354px;height:88px"></div>
    <div class="brand">veltaro</div><div class="pg">11</div>
    <div class="h" style="left:29px;top:40px">Fiktives Praxisbeispiel 2:<br><span class="tp">Automatisiertes<br>Mahnwesen</span></div>
    <div class="sub" style="left:193px;top:60px">Beispiel – Automatisierung des<br>Debitorenmanagements</div>
    <div class="card" style="left:30px;top:98px;width:130px;height:24px">Firma B, ein Dienstleistungsunternehmen</div>
    <div class="card" style="left:30px;top:131px;width:130px;height:32px">Ausgangslage: Verzögerte Zahlungseingänge, manuelle Verfolgung der offenen Forderungen</div>
    <div class="card" style="left:180px;top:98px;width:150px;height:30px">Digitalisierungslösung: Implementierung eines automatisierten Mahnwesensystems, das Zahlungserinnerungen automatisch versendet</div>
    <div class="card" style="left:180px;top:135px;width:150px;height:24px">Ergebnis: Reduktion der Außenstände um 40 %, Verbesserung des Cashflows</div>
    <div class="foot">Digitalisierung und Prozessoptimierung in der Buchhaltung</div><div class="url">www.veltaro.de</div>
  </section>

  <!-- 14 chart -->
  <section class="slide">
    <div class="brand">veltaro</div><div class="pg">11</div>
    <svg style="position:absolute;left:0;top:0" width="354" height="200" viewBox="0 0 354 200">
      <g font-size="6" fill="#2c3b47" text-anchor="middle">
        <text x="120" y="46">Außenstände (in %)</text><text x="255" y="46">Cashflow (in %)</text>
      </g>
      <g font-size="5" fill="#2c3b47">
        <text x="49" y="112" transform="rotate(-90 49 112)" text-anchor="middle">Prozent</text>
        <text x="184" y="112" transform="rotate(-90 184 112)" text-anchor="middle">Prozent</text>
      </g>
      <g stroke="#cfd3d7" stroke-width=".5">
        <line x1="63" y1="54" x2="63" y2="165"/><line x1="63" y1="165" x2="175" y2="165"/>
        <line x1="198" y1="54" x2="198" y2="165"/><line x1="198" y1="165" x2="310" y2="165"/>
      </g>
      <g font-size="4" fill="#2c3b47" text-anchor="end">
        <text x="61" y="57">100</text><text x="61" y="80">80</text><text x="61" y="102">60</text><text x="61" y="124">40</text><text x="61" y="146">20</text>
        <text x="196" y="57">140</text><text x="196" y="72">120</text><text x="196" y="88">100</text><text x="196" y="104">80</text><text x="196" y="120">60</text><text x="196" y="136">40</text><text x="196" y="151">20</text>
      </g>
      <rect x="68" y="55" width="48" height="110" fill="#123d5a"/>
      <rect x="124" y="99" width="48" height="66" fill="#a39a8f"/>
      <rect x="203" y="87" width="48" height="78" fill="#123d5a"/>
      <rect x="259" y="55" width="48" height="110" fill="#a39a8f"/>
      <g font-size="4" fill="#2c3b47" text-anchor="middle">
        <text x="92" y="171">Vorher</text><text x="148" y="171">Nachher</text>
        <text x="227" y="171">Vorher</text><text x="283" y="171">Nachher</text>
      </g>
    </svg>
    <div class="foot">Digitalisierung und Prozessoptimierung in der Buchhaltung</div><div class="url">www.veltaro.de</div>
  </section>

  <!-- 15 case 3 -->
  <section class="slide on-navy">
    <div class="navy-fill" style="left:0;top:100px;width:354px;height:100px"></div>
    <div class="brand">veltaro</div><div class="pg">11</div>
    <div class="h" style="left:27px;top:20px">Fiktives Praxisbeispiel 3:<br><span class="tp">Automatisierung der<br>Reisekostenabrechnung</span></div>
    <div class="sub" style="left:27px;top:58px">Beispiel – Automatisierung der<br>Reisekostenabrechnung</div>
    <div class="card" style="left:22px;top:84px;width:134px;height:16px;padding:4px 8px">Firma C, ein großes Bauunternehmen</div>
    <div class="card" style="left:22px;top:112px;width:134px;height:60px">Ausgangslage: Schickt regelmäßig Mitarbeiter auf Geschäftsreisen. Die Reisekostenabrechnung erfolgt durch manuelle Eingabe und Prüfung von Belegen, was zu langen Bearbeitungszeiten und häufiger Fehleranfälligkeit führt</div>
    <div class="card" style="left:180px;top:30px;width:152px;height:72px">Digitalisierungslösung: Einführung einer digitalen Lösung für die Reisekostenabrechnung, die automatisierte Belege scannt und die Spesenabrechnung in Echtzeit vergleicht. Die Mitarbeiter laden ihre Belege direkt in eine App hoch, und das System übernimmt die automatische Berechnung und Zuordnung der Kosten zu den entsprechenden Projekten.</div>
    <div class="card" style="left:180px;top:112px;width:152px;height:70px">Ergebnis: Firma C konnte die Bearbeitungszeit der Reisekostenabrechnungen um 60 % reduzieren. Die Fehlerrate sank nahezu auf null, und die Transparenz in der Abrechnung wurde erheblich verbessert. Zudem sind die Abrechnungen jetzt schneller abgeschlossen, was sich positiv auf die Cashflow-Planung auswirkt.</div>
    <div class="foot">Digitalisierung und Prozessoptimierung in der Buchhaltung</div><div class="url">www.veltaro.de</div>
  </section>

  <!-- 16 four charts -->
  <section class="slide">
    <div class="brand">veltaro</div><div class="pg">11</div>
    <svg style="position:absolute;left:0;top:0" width="354" height="200" viewBox="0 0 354 200">
      <g font-size="3.5" fill="#2c3b47" text-anchor="middle">
        <text x="72" y="74">Bearbeitungszeit (in %)</text><text x="150" y="74">Fehlerquote (in %)</text>
        <text x="228" y="74">Transparenz (in %)</text><text x="306" y="74">Cashflow-Planung (in %)</text>
        <text x="30" y="112" transform="rotate(-90 30 112)">Prozent</text>
      </g>
      <g stroke="#cfd3d7" stroke-width=".5">
        <line x1="40" y1="78" x2="40" y2="142"/><line x1="40" y1="142" x2="104" y2="142"/>
        <line x1="118" y1="78" x2="118" y2="142"/><line x1="118" y1="142" x2="182" y2="142"/>
        <line x1="196" y1="78" x2="196" y2="142"/><line x1="196" y1="142" x2="260" y2="142"/>
        <line x1="274" y1="78" x2="274" y2="142"/><line x1="274" y1="142" x2="338" y2="142"/>
      </g>
      <rect x="44" y="80" width="26" height="62" fill="#123d5a"/><rect x="75" y="117" width="26" height="25" fill="#a39a8f"/>
      <rect x="122" y="80" width="26" height="62" fill="#123d5a"/><rect x="153" y="141" width="26" height="1" fill="#a39a8f"/>
      <rect x="200" y="111" width="26" height="31" fill="#123d5a"/><rect x="231" y="80" width="26" height="62" fill="#a39a8f"/>
      <rect x="278" y="102" width="26" height="40" fill="#123d5a"/><rect x="309" y="80" width="26" height="62" fill="#a39a8f"/>
      <g font-size="3" fill="#2c3b47" text-anchor="middle">
        <text x="57" y="147">Vorher</text><text x="88" y="147">Nachher</text>
        <text x="135" y="147">Vorher</text><text x="166" y="147">Nachher</text>
        <text x="213" y="147">Vorher</text><text x="244" y="147">Nachher</text>
        <text x="291" y="147">Vorher</text><text x="322" y="147">Nachher</text>
      </g>
    </svg>
    <div class="foot">Digitalisierung und Prozessoptimierung in der Buchhaltung</div><div class="url">www.veltaro.de</div>
  </section>

  <!-- 17 Vorteile Digitalisierung -->
  <section class="slide">
    <div class="photo" style="left:212px;top:0;width:142px;height:200px;background:linear-gradient(180deg,#5c7283,#22455f 60%,#e8eaec 100%)" role="img" aria-label="Foto: Geschäftsleute bei einer Besprechung"></div>
    <div class="brand on-dark">veltaro</div><div class="pg">11</div>
    <div class="h" style="left:27px;top:50px">Vorteile der<br>Digitalisierung<br><span class="tp">und Prozessoptimierung</span></div>
    <div style="position:absolute;left:27px;top:98px;width:2px;height:22px;background:var(--navy)"></div>
    <div class="sub" style="left:35px;top:98px">Vorteile der Digitalisierung<br>in der Buchhaltung</div>
    <ul class="list" style="left:0;top:0">
      <li class="pill" style="left:188px;top:48px;width:135px">Zeitersparnis durch Automatisierung</li>
      <li class="pill" style="left:188px;top:78px;width:135px">Reduzierung von Fehlern und manuellen Eingriffen</li>
      <li class="pill" style="left:188px;top:114px;width:135px">Echtzeit-Reporting und verbesserte Entscheidungsgrundlagen</li>
      <li class="pill" style="left:188px;top:150px;width:135px">Einhaltung von Compliance-Richtlinien durch automatische Dokumentation</li>
    </ul>
    <div class="foot">Digitalisierung und Prozessoptimierung in der Buchhaltung</div><div class="url">www.veltaro.de</div>
  </section>

  <!-- 18 Vorteile Prozess -->
  <section class="slide">
    <div class="photo" style="left:212px;top:0;width:142px;height:200px;background:linear-gradient(180deg,#5c7283,#22455f 60%,#e8eaec 100%)" role="img" aria-label="Foto: Geschäftsleute bei einer Besprechung"></div>
    <div class="brand on-dark">veltaro</div><div class="pg">11</div>
    <div class="h" style="left:27px;top:50px">Vorteile der<br>Digitalisierung<br><span class="tp">und Prozessoptimierung</span></div>
    <div style="position:absolute;left:27px;top:98px;width:2px;height:22px;background:var(--navy)"></div>
    <div class="sub" style="left:35px;top:98px">Vorteile der Prozessoptimierung<br>durch Automatisierung</div>
    <ul class="list" style="left:0;top:0">
      <li class="pill" style="left:188px;top:78px;width:135px">Optimierung der Ressourcennutzung</li>
      <li class="pill" style="left:188px;top:106px;width:135px">Verbesserte Transparenz und Nachvollziehbarkeit</li>
      <li class="pill" style="left:188px;top:140px;width:135px">Verbesserung der Kundenzufriedenheit durch schnellere Verarbeitung</li>
    </ul>
    <div class="foot">Digitalisierung und Prozessoptimierung in der Buchhaltung</div><div class="url">www.veltaro.de</div>
  </section>

  <!-- 19 Herausforderungen -->
  <section class="slide">
    <div class="brand">veltaro</div><div class="pg">11</div>
    <div class="h" style="left:35px;top:38px">Herausforderungen<br><span class="tp">bei der Umsetzung</span></div>
    <div class="sub" style="left:35px;top:70px">Herausforderungen bei der Digi-<br>talisierung in der Buchhaltung</div>
    <ul class="list" style="left:35px;top:96px;width:130px">
      <li>Mangelnde IT-Kompetenzen im Team</li>
      <li>Hohe Implementierungskosten für neue Systeme</li>
      <li>Widerstand der Mitarbeiter gegen Veränderungen</li>
    </ul>
    <div class="photo circle" style="left:189px;top:34px;width:144px;height:144px;background:linear-gradient(135deg,#cfd6dc,#4a5a68)" role="img" aria-label="Foto: Geschäftsfrau mit Tablet"></div>
    <div class="sq" style="left:318px;top:166px"></div>
    <div class="foot">Digitalisierung und Prozessoptimierung in der Buchhaltung</div><div class="url">www.veltaro.de</div>
  </section>

  <!-- 20 Herausforderungen Strategien -->
  <section class="slide">
    <div class="brand">veltaro</div><div class="pg">10</div>
    <div class="photo circle" style="left:17px;top:28px;width:144px;height:144px;background:linear-gradient(135deg,#cfd6dc,#4a5a68)" role="img" aria-label="Foto: Geschäftsfrau mit Tablet"></div>
    <div class="sq" style="left:146px;top:156px"></div>
    <div class="h" style="left:184px;top:48px">Herausforderungen<br><span class="tp">bei der Umsetzung</span></div>
    <div class="sub" style="left:184px;top:80px">Strategien zur Überwindung von<br>Hindernissen</div>
    <ul class="list" style="left:184px;top:106px;width:158px">
      <li>Schulung der Mitarbeiter und Change Management</li>
      <li>Schrittweise Implementierung statt radikaler Umstellungen</li>
      <li>Auswahl der richtigen Partner und Technologien</li>
    </ul>
    <div class="foot">Digitalisierung und Prozessoptimierung in der Buchhaltung</div><div class="url">www.veltaro.de</div>
  </section>

  <!-- 21 Zukunft tiles -->
  <section class="slide">
    <div class="brand">veltaro</div><div class="pg">11</div>
    <div class="h" style="left:33px;top:40px">Zukunft der<br>Digitalisierung <span class="tp">in</span><br><span class="tp">der Buchhaltung</span></div>
    <div class="tab" style="left:152px;top:36px;width:80px;height:80px;border-radius:10px 0 0 0;padding:12px 10px;font-size:6.5px;text-transform:none;line-height:1.3">Trends in der<br>Digitalisierung<br>der Buchhaltung</div>
    <div class="photo" style="left:235px;top:36px;width:80px;height:80px;border-radius:0 10px 0 0;background:linear-gradient(180deg,#7d8f9d,#3b566b)" role="img" aria-label="Bild: Server und Datennetz als Symbol für künstliche Intelligenz"></div>
    <div style="position:absolute;left:241px;top:78px;width:70px;font-size:5.5px;color:#fff">Zunehmende Bedeutung von Künstlicher Intelligenz und Machine Learning</div>
    <div class="photo" style="left:152px;top:119px;width:80px;height:78px;border-radius:0 0 0 10px;background:linear-gradient(180deg,#8898a5,#2f4a60)" role="img" aria-label="Foto: Geschäftsmann mit Laptop"></div>
    <div style="position:absolute;left:158px;top:170px;width:70px;font-size:5.5px;color:#fff">Blockchain für sichere, nachvollziehbare Buchführung</div>
    <div class="photo" style="left:235px;top:119px;width:80px;height:78px;border-radius:0 0 10px 0;background:linear-gradient(180deg,#9aa7b2,#2f4a60)" role="img" aria-label="Foto: Geschäftsmann arbeitet am Laptop"></div>
    <div style="position:absolute;left:241px;top:170px;width:70px;font-size:5.5px;color:#fff">Automatisierte Steuererklärung und Compliance-Prüfungen</div>
    <div class="foot">Digitalisierung und Prozessoptimierung in der Buchhaltung</div>
  </section>

  <!-- 22 Zukunft best practices -->
  <section class="slide">
    <div class="brand">veltaro</div><div class="pg">11</div>
    <div class="tab" style="left:31px;top:26px;width:128px;height:148px;border-radius:12px;padding:98px 0 0 12px;font-size:9.5px;line-height:1.2">Zukunft der<br>Digitalisierung <span style="color:var(--taupe)">in<br>der Buchhaltung</span></div>
    <div class="sub" style="left:190px;top:70px">Best Practices bei der Einführung<br>digitaler Buchhaltungssysteme</div>
    <ul class="list" style="left:190px;top:96px;width:140px">
      <li>Klare Ziele setzen und den ROI messen</li>
      <li>Interdisziplinäre Zusammenarbeit zwischen Buchhaltung und IT</li>
      <li>Regelmäßige Überprüfung und Anpassung der Prozesse</li>
    </ul>
    <div class="foot">Digitalisierung und Prozessoptimierung in der Buchhaltung</div><div class="url">www.veltaro.de</div>
  </section>

  <!-- 23 Zusammenfassung -->
  <section class="slide">
    <div class="brand">veltaro</div><div class="pg">11</div>
    <div class="h" style="left:34px;top:36px">Zusammenfassung <span class="tp">und Ausblick</span></div>
    <div class="sub" style="left:36px;top:70px">Zusammenfassung der<br>wichtigsten Erkenntnisse</div>
    <div style="position:absolute;left:168px;top:72px;width:144px">
      <p style="padding-bottom:6px;border-bottom:.5px solid #ccc">Bedeutung der Digitalisierung für die Effizienz und Fehlerreduktion</p>
      <p style="padding:6px 0;border-bottom:.5px solid #ccc">Erfolgsfaktoren: Technologieauswahl, Schulung, und schrittweise Umsetzung</p>
      <p style="padding-top:6px">Ausblick: Die Zukunft der Buchhaltung ist digital</p>
    </div>
    <div class="foot">Digitalisierung und Prozessoptimierung in der Buchhaltung</div><div class="url">www.veltaro.de</div>
  </section>

  <!-- 24 Fragen -->
  <section class="slide">
    <div class="photo" style="left:0;top:0;width:354px;height:200px;background:linear-gradient(135deg,#7f8c97,#c9bfb3 50%,#5a6f80)" role="img" aria-label="Foto: lachende Teilnehmer in einem Seminar"></div>
    <div class="tab" style="left:0;top:0;width:90px;height:40px;border-radius:0 0 12px 0;padding:8px 0 0 23px;font-size:9.5px;line-height:1.2">Fragen und<br>Antworten</div>
    <div style="position:absolute;left:90px;top:125px;width:244px;height:60px;border-radius:10px;background:rgba(18,61,90,.85);color:#fff;padding:8px 12px;font-size:8px;line-height:1.35">
      Fragen und Diskussion<br><span style="color:#dfe6eb">Interaktive Fragenrunde, in der die Teilnehmer ihre Fragen stellen können</span>
    </div>
  </section>

  <!-- 25 Danke -->
  <section class="slide">
    <div class="photo" style="left:0;top:0;width:174px;height:200px;background:linear-gradient(135deg,#a3adb6,#45596a)" role="img" aria-label="Foto: lächelnder Geschäftsmann mit verschränkten Armen"></div>
    <div class="navy-fill" style="left:174px;top:0;width:180px;height:150px"></div>
    <div style="position:absolute;right:14px;top:22px;text-align:right;color:#fff;font-size:12.5px;line-height:1.35;text-transform:uppercase">Vielen Dank<br>für Ihre<br><span style="color:var(--taupe)">Aufmerksamkeit</span></div>
    <div style="position:absolute;right:14px;top:84px;text-align:right;color:#fff;font-size:4.6px;line-height:1.5">
      <b>VELTARO, Inh. Lukas Brenner</b><br><br>Ahornweg 12<br>85540 Haar<br><br>Tel.: +49 89 5550172<br>E-Mail: info@veltaro.de<br>Internet: www.veltaro.de
    </div>
    <div style="position:absolute;right:14px;top:165px;font-weight:600;font-size:20px;color:var(--navy);line-height:1">veltaro</div>
  </section>

</main>
</body>
</html>
```